I want both print and ebook covers

book title is "The Classroom MEETING HANDBOOK: Fresh Paths to Partner With Families For Student Growth. I want a dark Teal or Navy Background. Yellow and white letters. Distorted Picture of one teacher, two parents and one child around a table or desk. But no Martians! My name should include "Award Winning Author"

Target Market(s)

teachers and other educators--principals, school psychologists, speech therapists, etc.

Industry/Entity Type

schools

Font styles to use
Other font styles liked:
• I just need to see how it looks

Colors
0054AA
0677BA
7BADD7
CADEEF
E8F1F8
0094D4
00A9DD
6FCCEA
C7EBF8
E9F6FB
FFC000
F8CF3A
FAE287
FDF2CF
FEFAEE

Requirements
Must have
• Title top third of page big enough to be read when reduced greatly in size. Contrast so that it "pops'.
Nice to have
• Teacher, two parents and one child around a table/desk. My name should include 'Award winning author'

```html
<!DOCTYPE html>
<html lang="en">
<head>
<meta charset="utf-8">
<title>The Classroom Meeting Handbook – Cover</title>
<link rel="stylesheet" href="https://fonts.googleapis.com/css2?family=Permanent+Marker&family=Bebas+Neue&family=Tinos&family=Montserrat:wght@500&display=swap">
<style>
  :root {
    --gold: #fdb923;
    --title-gold: #ffc000;
    --author-gold: #f8cf3a;
    --navy: #0b0d4f;
    --teal-deep: #063a52;
    --teal-mid: #0a5a78;
    --teal-glow: #0d6f8f;
    --white: #ffffff;
  }
  * { margin: 0; padding: 0; box-sizing: border-box; }
  html, body { width: 800px; height: 1200px; overflow: hidden; background: var(--navy); }
  .cover { position: relative; width: 800px; height: 1200px; overflow: hidden; }

  .cover-scene {
    position: absolute; left: 0; top: 0; width: 800px; height: 843px;
    background:
      radial-gradient(ellipse 480px 320px at 400px 440px, var(--teal-glow) 0%, rgba(13,111,143,0) 100%),
      linear-gradient(170deg, var(--teal-mid) 0%, var(--teal-deep) 55%, var(--navy) 100%);
  }

  .title {
    position: absolute; left: 60px; top: 250px; width: 680px;
    transform: rotate(3deg);
    font-family: "Permanent Marker", "Marker Felt", "Comic Sans MS", cursive;
    font-weight: 400;
    color: var(--title-gold);
    text-align: center;
    line-height: 1.1;
    text-transform: uppercase;
    text-shadow: 0 3px 10px rgba(0, 0, 0, 0.35);
  }
  .title-line { display: block; }
  .title-small { font-size: 70px; }
  .title-large { font-size: 100px; }

  .subtitle-band {
    position: absolute; left: 0; top: 843px; width: 800px; height: 180px;
    background: var(--gold);
    display: flex; flex-direction: column; justify-content: center; align-items: center;
    font-family: "Bebas Neue", "Oswald", sans-serif;
    color: var(--white);
    font-size: 56px; line-height: 1.2;
    text-align: center;
  }

  .author-band {
    position: absolute; left: 0; top: 1023px; width: 800px; height: 177px;
    background: var(--navy);
    text-align: center;
  }
  .author-name {
    position: absolute; left: 0; right: 0; top: 30px;
    font-family: "Tinos", "Times New Roman", serif;
    font-size: 64px;
    color: var(--author-gold);
  }
  .author-credit {
    position: absolute; left: 0; right: 0; top: 118px;
    font-family: "Montserrat", sans-serif;
    font-weight: 500;
    font-size: 21px;
    letter-spacing: 0.5em;
    padding-left: 0.5em;
    color: var(--author-gold);
  }
</style>
</head>
<body>
  <div class="cover">
    <div class="cover-scene" role="img" aria-label="Soft dark teal backdrop for a classroom desk scene"></div>

    <h1 class="title">
      <span class="title-line title-small">The Classroom</span>
      <span class="title-line title-large">Meeting</span>
      <span class="title-line title-large">Handbook</span>
    </h1>

    <div class="subtitle-band">
      <p class="subtitle-line">Fresh Paths to Partner With Families</p>
      <p class="subtitle-line">For Student Growth</p>
    </div>

    <div class="author-band">
      <p class="author-name">Marian Ellis Holt Ph.D.</p>
      <p class="author-credit">AWARD WINNING AUTHOR</p>
    </div>
  </div>
</body>
</html>
```